Combat Sports news website design

Redesigning our existing website to make it more modern, responsive and suitable for our needs. The design needs to take in to account all aspects of our current website structure and services. View the existing website at https://www.brawlpulse.co.nz

Particular attention should be paid to our livestream service, which is growing and needs to be much more user friendly to the current experience.

The homepage, article listings and article pages need designs.

Target Market(s)

Combat sports fans

Industry/Entity Type

Media

Coding

Number of Pages Required

5+ page

Font styles to use
Sans Serif

Requirements
Must have
• All the functionality of the existing website must be taken in to account, and improved upon.
New design must incorporate our existing logo/colour scheme as this has only just been designed.

```html
<!DOCTYPE html>
<html lang="en">
<head>
<meta charset="utf-8">
<title>Tane Whitlock steps into Crest 80kg division on short notice — Brawl Pulse</title>
<link href="https://fonts.googleapis.com/css2?family=Montserrat:wght@400;500;600;700;800&family=Oswald:wght@500;600;700&display=swap" rel="stylesheet">
<style>
:root{
  --red:#c8202f;
  --ink:#1f1f1f;
  --text:#3a3a3a;
  --muted:#777;
  --panel:#f4f4f4;
  --nav:#1a1a1a;
  --subnav:#2a2a2a;
  --footer:#1c1c1c;
  --footer-text:#9a9a9a;
}
*{box-sizing:border-box;margin:0;padding:0}
html,body{width:1200px;height:4452px;overflow:hidden}
body{font-family:"Montserrat",sans-serif;color:var(--text);background:#fff;position:relative}
a{color:inherit;text-decoration:none}

/* header */
.hero{position:absolute;left:0;top:0;width:1200px;height:622px;background:linear-gradient(120deg,#3a2e22 0%,#5a4630 35%,#2b2420 60%,#4b3a26 100%)}
.hero-shade{position:absolute;inset:0;background:rgba(0,0,0,.35)}
.topbar{position:absolute;left:0;top:0;width:1200px;height:60px;background:rgba(20,20,20,.92);font-family:"Oswald",sans-serif;color:#fff;font-size:15px;letter-spacing:.3px}
.topbar a{position:absolute;top:20px;text-transform:uppercase}
.topbar .active{font-size:19px;top:16px}
.topbar .active::after{content:"";position:absolute;left:0;right:0;bottom:-20px;height:3px;background:var(--red)}
.brand{position:absolute;left:566px;top:10px;font-family:"Oswald",sans-serif;font-weight:700;font-size:20px;line-height:19px;color:#fff;text-align:left}
.search{position:absolute;left:1094px;top:20px}
.subnav{position:absolute;left:0;top:60px;width:1200px;height:48px;background:rgba(40,40,40,.85);font-family:"Oswald",sans-serif;font-size:14px;color:#bbb}
.subnav a{position:absolute;top:14px;text-transform:uppercase}
.subnav .on{color:#fff}
.hero h1{position:absolute;left:211px;top:266px;width:760px;font-weight:800;font-size:43px;line-height:51px;color:#fff;text-transform:uppercase;letter-spacing:.5px}

/* share bar */
.sharebar{position:absolute;left:444px;top:644px;display:flex;align-items:center;gap:22px;font-size:13px;font-weight:600;color:var(--ink)}
.sharebar .count{padding-right:14px;border-right:1px solid #ccc}
.sq{width:15px;height:15px;background:#333;border-radius:2px}

/* article */
.article{position:absolute;left:99px;top:700px;width:632px}
.meta{font-size:12px;color:#444;display:flex;align-items:center;gap:10px;margin-bottom:12px;text-transform:uppercase}
.meta:first-child{text-transform:none}
.article p{font-size:16px;line-height:20px;color:#444}
.article p.lead{font-weight:700;color:var(--ink)}
.article h3{font-size:18px;font-weight:700;line-height:22px;color:var(--ink)}
.quote{background:var(--panel);border-left:9px solid var(--red);padding:0 60px 0 24px;display:flex;align-items:center;font-size:14px;line-height:18px;color:#555}
.photo{width:632px;height:420px;background:linear-gradient(135deg,#5a5048,#8a7a6a 40%,#3e3934 75%,#2a2624)}
.caption{text-align:center;font-size:12.5px;letter-spacing:.6px;color:#555;line-height:16px;text-transform:uppercase;padding:0 60px}
.article p a{color:var(--red)}

/* post nav */
.postnav{position:absolute;left:99px;top:2960px;width:640px;display:flex;justify-content:space-between}
.postnav .col{width:260px}
.postnav .col.next{width:240px}
.postnav .lbl{font-size:22px;font-weight:800;color:var(--red);display:flex;align-items:center;gap:10px}
.postnav .next .lbl{justify-content:flex-end}
.postnav .t{font-size:12px;font-weight:500;color:var(--ink);margin-top:14px;line-height:15px;text-transform:uppercase}

.section-title{font-size:21px;font-weight:800;color:var(--ink);border-left:7px solid var(--red);padding-left:11px;line-height:24px;text-transform:uppercase}

.related{position:absolute;left:99px;top:3114px;width:680px}
.related-grid{display:grid;grid-template-columns:357px 320px;row-gap:40px;margin-top:52px}
.rel{display:flex;gap:20px}
.thumb{width:133px;height:114px;flex:none}
.rel h4{font-size:12px;font-weight:700;line-height:15px;color:var(--ink);margin-top:12px;text-transform:uppercase}
.rel .time{font-size:10px;color:#666;margin-top:10px;display:flex;align-items:center;gap:6px}
.rel .more{font-size:11px;color:var(--red);margin-top:12px;letter-spacing:.5px}

.comments{position:absolute;left:99px;top:3525px;width:640px}
.board{margin-top:50px;width:636px;font-size:12px;color:#555}
.board-top{display:flex;justify-content:space-between;border-bottom:2px solid #e4e4e4;padding-bottom:8px}
.board-top b{color:#333}
.board-row{display:flex;justify-content:space-between;margin-top:12px;font-size:11px}
.pill{display:inline-block;background:#3b7bd6;color:#fff;font-size:10px;padding:1px 8px;border-radius:3px;margin-left:6px}
.compose{display:flex;gap:14px;margin-top:22px}
.avatar{width:36px;height:36px;background:#bfc3c7;border-radius:3px}
.input{flex:1;height:38px;border:1px solid #cfd3d6;border-radius:4px;padding:10px;color:#888;font-size:14px}
.login{display:flex;gap:90px;margin:10px 0 0 50px;font-size:9px;color:#666;text-transform:uppercase}
.dots{display:flex;gap:6px;margin-top:8px}
.dots i{width:26px;height:26px;border-radius:50%;display:block}
.namebox{width:438px;height:26px;border:1px solid #cfd3d6;border-radius:3px;margin-top:8px;padding:5px 8px;font-size:10px;color:#999}
.first{text-align:center;margin-top:80px;font-size:12px;color:#888}
.board-foot{display:flex;gap:34px;align-items:center;margin-top:48px;font-size:10px;color:#555}
.board-foot .mark{margin-left:auto;font-weight:800;font-size:17px;color:#555;letter-spacing:1px}

/* sidebar */
.box{position:absolute;background:var(--panel);padding:26px 22px}
.box h5{font-size:14px;font-weight:700;color:var(--ink);border-left:6px solid var(--red);padding-left:10px;letter-spacing:.8px;text-transform:uppercase;line-height:17px}
.headlines{left:806px;top:697px;width:297px;height:579px}
.headlines ul{list-style:none;margin-top:26px}
.headlines li{margin-bottom:24px}
.headlines li a{font-size:12.5px;line-height:16px;color:var(--red);display:block}
.headlines .time{display:flex;gap:8px;align-items:center;font-size:9px;color:#555;margin-top:6px}
.ad{left:801px;width:300px;height:243px}
.ad .slot{width:250px;height:161px;background:#c9c9c9;margin-top:26px}
.follow{left:801px;top:1584px;width:300px;height:173px}
.follow .btns{display:flex;flex-wrap:wrap;gap:14px 14px;margin-top:22px}
.fbtn{width:120px;height:33px;color:#fff;font-size:11px;font-weight:700;display:flex;align-items:center;justify-content:center;gap:8px;letter-spacing:.5px}
.fbtn i{width:12px;height:12px;background:#fff;border-radius:50%;display:block}
.poll{left:799px;top:2059px;width:302px;height:400px}
.poll .q{font-size:13px;font-weight:700;color:var(--ink);margin-top:20px;line-height:16px}
.poll ul{list-style:none;margin-top:22px}
.poll li{display:flex;align-items:center;gap:18px;font-size:12px;font-weight:700;color:var(--ink);margin-bottom:15px;height:26px}
.radio{width:26px;height:26px;border:2px solid var(--red);border-radius:50%;display:flex;align-items:center;justify-content:center}
.radio.sel::after{content:"";width:16px;height:16px;background:var(--red);border-radius:50%}
.poll .actions{display:flex;gap:10px;margin-top:20px}
.poll .actions span{background:var(--red);color:#fff;font-size:11px;padding:10px 24px;letter-spacing:.5px}

/* footer */
.footer{position:absolute;left:0;top:4043px;width:1200px;height:409px;background:var(--footer);color:var(--footer-text);font-size:13px}
.footer .logo{position:absolute;left:83px;top:26px;font-family:"Oswald",sans-serif;font-weight:700;font-size:44px;line-height:44px;color:var(--red)}
.footer .who{position:absolute;left:83px;top:154px;width:243px}
.footer .who strong{display:block;font-size:18px;color:#ddd;margin-bottom:2px}
.footer .who p{font-size:12.5px;line-height:14.5px;text-align:justify}
.fcol{position:absolute;top:40px}
.fcol h6{font-size:12px;font-weight:600;color:#555;margin-bottom:12px;letter-spacing:.5px;text-transform:uppercase}
.fcol li{list-style:none;color:#ddd;font-size:14px;line-height:21px}
.touch{position:absolute;left:453px;top:280px}
.touch .icons{display:flex;gap:34px;margin-top:14px}
.touch .icons i{width:20px;height:20px;background:#bbb;display:block;border-radius:3px}
.field{width:178px;height:22px;background:#3a3a3a;color:#bbb;font-size:10px;padding:5px 10px;margin-bottom:9px}
.field.msg{width:256px;height:152px}
.submit{background:var(--red);color:#fff;font-weight:700;font-size:14px;width:78px;height:24px;text-align:center;line-height:24px;margin-top:12px}
.copy{position:absolute;left:83px;top:382px;font-size:9px;color:#777}
.help{position:absolute;left:453px;top:376px;display:flex;align-items:center;gap:10px;font-size:13px;color:#ddd}
.help span{color:#555;font-weight:600;font-size:12px}
</style>
</head>
<body>

<header>
  <div class="hero" role="img" aria-label="Two fighters exchanging punches in a ring under arena lights, a referee watching">
    <div class="hero-shade"></div>
  </div>
  <nav class="topbar">
    <a style="left:138px">Home</a>
    <a class="active" style="left:244px">Categories</a>
    <a style="left:389px">Live events</a>
    <div class="brand">BRAWL<br>PULSE</div>
    <a style="left:743px">Contact us</a>
    <a style="left:852px">About us</a>
    <a style="left:960px">Login / Register</a>
    <svg class="search" width="20" height="20" viewBox="0 0 20 20"><circle cx="8" cy="8" r="6" fill="none" stroke="#fff" stroke-width="2"/><path d="M12.5 12.5 18 18" stroke="#fff" stroke-width="2"/></svg>
  </nav>
  <nav class="subnav">
    <a style="left:138px">MMA</a>
    <a class="on" style="left:197px">Kickboxing</a>
    <a style="left:296px">Boxing</a>
    <a style="left:365px">Wrestling</a>
    <a style="left:456px">UCW</a>
    <a style="left:513px">PROFC</a>
  </nav>
  <h1>Tane Whitlock steps into Crest 80kg division on short notice</h1>
</header>

<div class="sharebar">
  <span class="count">417 Shares</span>
  <i class="sq"></i><i class="sq"></i><i class="sq"></i><i class="sq"></i>
  <svg width="18" height="16" viewBox="0 0 18 16"><rect x="4" y="0" width="10" height="5" fill="#333"/><rect x="0" y="5" width="18" height="7" rx="1" fill="#333"/><rect x="4" y="10" width="10" height="6" fill="#fff" stroke="#333" stroke-width="1.5"/></svg>
  <svg width="18" height="14" viewBox="0 0 18 14"><rect width="18" height="14" rx="1" fill="#333"/><path d="M1 1l8 6 8-6" fill="none" stroke="#fff" stroke-width="1.5"/></svg>
</div>

<article class="article">
  <div class="meta"><svg width="18" height="18" viewBox="0 0 18 18"><circle cx="9" cy="9" r="7.5" fill="none" stroke="#555" stroke-width="1.4"/><path d="M9 4.5V9l3 2" fill="none" stroke="#555" stroke-width="1.4"/></svg>7:30AM THURSDAY 29 APR, 2021</div>
  <div class="meta"><svg width="18" height="18" viewBox="0 0 18 18"><circle cx="9" cy="9" r="7.5" fill="none" stroke="#555" stroke-width="1.4"/><circle cx="9" cy="7" r="2.5" fill="none" stroke="#555" stroke-width="1.4"/><path d="M4.5 14c1-2.5 8-2.5 9 0" fill="none" stroke="#555" stroke-width="1.4"/></svg>Sam Ashby sam@brawlpulse.co.nz</div>

  <p class="lead" style="margin-top:30px">Tane Whitlock is stepping in on short notice to replace the injured Marco Reyes against Kauri Matene-Hill, in the 80kg division of the Crest Muay Thai Warrior Series this Saturday, May 1.</p>
  <p class="lead" style="margin-top:22px">Reyes suffered a knee tear in sparring during preparation for his fight, which forced promoter Dean Harlow to find a late-notice replacement.</p>
  <p style="margin-top:41px">Luckily, Whitlock answered the call. He was scheduled to fight Jory Pennell for a New Zealand full Thai rules title the following weekend.</p>
  <p style="margin-top:29px">Fighting out of Summit Muay Thai in Porirua, 38-year-old Whitlock is a 20-fight veteran, winning a SKL South Island title in 2018.</p>
  <p style="margin-top:15px">Brawl Pulse caught up with Tane Whitlock to ask him a few questions ahead of this Saturday's fight.</p>
  <h3 style="margin-top:26px">You're stepping in on short notice to face Kauri this Saturday. What went through your mind when you got the call-up?</h3>
  <div class="quote" style="margin-top:44px;height:141px">I was actually supposed to be fighting next weekend, on our show, but my guy pulled out yesterday. Then I got the cold call from Dean [Harlow, promoter] and I was like 'f*ck yes, I want to fight, awesome'.</div>
  <h3 style="margin-top:30px">Have you faced anyone in the line-up before?</h3>
  <div class="quote" style="margin-top:26px;height:114px">"I dunno who's in it, man. I actually don't know anything about it. All I know is I thought I didn't have a fight, was super disappointed, but then Dean rang up and now I've got a fight!</div>
  <div class="quote" style="margin-top:12px;height:115px">"I love these short notice ones; you don't know anything about who you're fighting. You just rock up and say what's up."</div>
  <h3 style="margin-top:34px">Did you have to change anything in your training camp once you knew you were fighting this weekend?</h3>
  <div class="quote" style="margin-top:45px;height:140px">"Yeah, I was supposed to be fighting a southpaw, haha. I'm a southpaw as well, so I've got my usual southpaw strategy which is what I'll go for, I'd say."</div>
  <div class="photo" style="margin-top:48px" role="img" aria-label="Whitlock landing a southpaw straight left on his opponent in the ring, referee behind"></div>
  <p class="caption" style="margin-top:12px">Whitlock lands the southpaw straight left at Clash 4 RA in 2018 (Photo: Ring Lens Studio)</p>
  <h3 style="margin-top:52px;font-size:16px">Thanks for your time Tane. All the best for Saturday!</h3>
  <p style="margin-top:12px">Crest Muay Thai Warrior Series #2 takes place this Saturday, May 1, from 5pm at Northline Sport Gym in Birkenhead, Auckland. VIP tickets are sold out, but there are still limited GA tickets available from TicketHop.</p>
  <p style="margin-top:23px">Crest Muay Thai Warrior Series #2 takes place this Saturday, May 1, from 5pm at Northline Sport Gym in Birkenhead, Auckland. VIP tickets are sold out, but there are still limited GA tickets available from TicketHop.</p>
  <p style="margin-top:19px">Crest Muay Thai Warrior Series #2 takes place this Saturday, May 1, from 5pm at Northline Sport Gym in Birkenhead, Auckland. VIP tickets are sold out, but there are still limited GA tickets available from TicketHop.</p>
  <p style="margin-top:31px">If you can't make it to the event, it will be live streamed on Brawl Pulse PPV. To subscribe, first <a>register an account on the Brawl Pulse site</a> , then activate it through the email link. Then <a>subscribe to the PPV here.</a></p>
</article>

<nav class="postnav">
  <div class="col">
    <div class="lbl"><svg width="26" height="18" viewBox="0 0 26 18"><path d="M25 9H3M10 2 3 9l7 7" fill="none" stroke="#c8202f" stroke-width="3"/></svg>PREVIOS POST</div>
    <div class="t">Five NKF New Zealand Cup winners crowned at Built to Fight 9</div>
  </div>
  <div class="col next">
    <div class="lbl">NEXT POST<svg width="26" height="18" viewBox="0 0 26 18"><path d="M1 9h22M16 2l7 7-7 7" fill="none" stroke="#c8202f" stroke-width="3"/></svg></div>
    <div class="t">Five NKF New Zealand Cup winners crowned at Built to Fight 9</div>
  </div>
</nav>

<section class="related">
  <h2 class="section-title">Related posts</h2>
  <div class="related-grid">
    <div class="rel">
      <div class="thumb" role="img" aria-label="Two fighters trading blows in a dim ring" style="background:linear-gradient(135deg,#3b342e,#7a6b5c)"></div>
      <div><h4>Hartwell predicts hard fight at Crest this Saturday</h4><div class="time"><svg width="12" height="12" viewBox="0 0 18 18"><circle cx="9" cy="9" r="7.5" fill="none" stroke="#555" stroke-width="1.6"/><path d="M9 4.5V9l3 2" fill="none" stroke="#555" stroke-width="1.6"/></svg>12:00PM WED 28 APR</div><div class="more">READ MORE →</div></div>
    </div>
    <div class="rel">
      <div class="thumb" role="img" aria-label="Fight night event poster with three fighters" style="background:linear-gradient(160deg,#1e2a4a,#3c4e7a 60%,#b78a2a)"></div>
      <div><h4>Hartwell predicts hard fight at Crest this Saturday</h4><div class="time"><svg width="12" height="12" viewBox="0 0 18 18"><circle cx="9" cy="9" r="7.5" fill="none" stroke="#555" stroke-width="1.6"/><path d="M9 4.5V9l3 2" fill="none" stroke="#555" stroke-width="1.6"/></svg>12:00PM WED 28 APR</div><div class="more">READ MORE →</div></div>
    </div>
    <div class="rel">
      <div class="thumb" role="img" aria-label="Heavyweight boxing bout promotional poster" style="background:linear-gradient(160deg,#2a2a2a,#5a5550 60%,#1b1b1b)"></div>
      <div><h4>Hartwell predicts hard fight at Crest this Saturday</h4><div class="time"><svg width="12" height="12" viewBox="0 0 18 18"><circle cx="9" cy="9" r="7.5" fill="none" stroke="#555" stroke-width="1.6"/><path d="M9 4.5V9l3 2" fill="none" stroke="#555" stroke-width="1.6"/></svg>12:00PM WED 28 APR</div><div class="more">READ MORE →</div></div>
    </div>
  </div>
</section>

<section class="comments">
  <h2 class="section-title">Comments</h2>
  <div class="board">
    <div class="board-top"><span><b>0 Comments</b> &nbsp;&nbsp;&nbsp; Brawl Pulse &nbsp;&nbsp;&nbsp;&nbsp; ChatBoard Privacy Policy</span><span style="color:#333">● Login ▾</span></div>
    <div class="board-row"><span><span style="color:var(--red)">♡ Recommend</span> <span class="pill">Tweet</span><span class="pill">Share</span></span><span>Sort by Best ▾</span></div>
    <div class="compose"><div class="avatar"></div><div class="input">Start the discussion…</div></div>
    <div class="login"><div>Log in with<div class="dots"><i style="background:#3b7bd6"></i><i style="background:#3b5998"></i><i style="background:#1da1f2"></i><i style="background:#db4437"></i></div></div><div>or sign up with ChatBoard ?<div class="namebox">Name</div></div></div>
    <div class="first">Be the first to comment.</div>
    <div class="board-foot"><span>✉ Subscribe</span><span>● Add ChatBoard to your site</span><span>▲ Do Not Sell My Data</span><span class="mark">CHATBOARD</span></div>
  </div>
</section>

<aside>
  <div class="box headlines">
    <h5>Latest headlines</h5>
    <ul>
      <li><a>Lani Brooks looking to avenge her only loss</a><div class="time">◷ 13:00PM &nbsp;WED 28 APR</div></li>
      <li><a>Tane Whitlock steps into Crest 80kg division on short notice</a><div class="time">◷ 12:00PM &nbsp;WED 28 APR</div></li>
      <li style="margin-bottom:34px"><a>Five NKF New Zealand Cup winners crowned at Built to Fight 9</a></li>
      <li style="margin-top:-22px"><div class="time">◷ 12:00PM &nbsp;WED 28 APR</div></li>
      <li><a>Hartwell predicts hard fight at Crest this Saturday</a><div class="time">◷ 12:00PM &nbsp;WED 28 APR</div></li>
      <li><a>Unbroken Fight Series 2 results</a><div class="time">◷ 12:00PM &nbsp;WED 28 APR</div></li>
      <li><a>VIDEO: "I'm bringing pain!" - Vince Okafor declares war on Liam Tautai</a><div class="time">◷ 12:00PM &nbsp;WED 28 APR</div></li>
    </ul>
  </div>

  <div class="box ad" style="top:1309px"><h5>Advertisement</h5><div class="slot"></div></div>

  <div class="box follow">
    <h5>Follow us</h5>
    <div class="btns">
      <span class="fbtn" style="background:#7a3fb0"><i></i>FOLLOW</span>
      <span class="fbtn" style="background:#1da1f2"><i></i>FOLLOW</span>
      <span class="fbtn" style="background:#3b5998"><i></i>FOLLOW</span>
    </div>
  </div>

  <div class="box ad" style="top:1784px"><h5>Advertisement</h5><div class="slot"></div></div>

  <div class="box poll">
    <h5>Opinion poll</h5>
    <p class="q">What combat sport do you prefer?</p>
    <ul>
      <li><span class="radio sel"></span>MMA</li>
      <li><span class="radio"></span>WRESTLING</li>
      <li><span class="radio"></span>KICKBOXING</li>
      <li><span class="radio"></span>MUAY THAI</li>
      <li><span class="radio"></span>ALL OF THE ABOVE</li>
    </ul>
    <div class="actions"><span>VOTE</span><span>SHOW RESULTS</span></div>
  </div>
</aside>

<footer class="footer">
  <div class="logo">BRAWL<br>PULSE</div>
  <div class="who"><strong>Mara Quinlan</strong><p>Mara has worked in the media industry since she was 15-years-old. She has worked in both radio and print, and is the co-founder and editor-in-chief of Brawl Pulse. As well as being the Brawl Pulse Editor, she focuses on writing for multi-discipline combat sports.</p></div>
  <div class="fcol" style="left:453px"><h6>Site map</h6><ul><li>Home</li><li>MMA</li><li>Kickboxing</li><li>Boxing</li><li>Wrestling</li><li>UCW</li><li>PROFC</li><li>Live events</li></ul></div>
  <div class="fcol" style="left:612px"><h6>Usefull links</h6><ul><li>Site Terms</li><li>Advertisement</li><li>Contact us</li><li>Privacy</li></ul></div>
  <div class="fcol" style="left:859px"><h6>Contact us</h6>
    <div class="field">First name</div><div class="field">Last name</div><div class="field">Email</div><div class="field">Phone / Mobile</div><div class="field msg">Message</div>
    <div class="submit">Submit</div>
  </div>
  <div class="touch"><h6 style="font-size:12px;color:#555;font-weight:600">GET IN TOUCH</h6><div class="icons"><i></i><i></i><i></i><i></i></div></div>
  <div class="copy">Copyright © 2021-2022 BRAWL PULSE All Rights Reserved</div>
  <div class="help"><span>NEED HELP?</span><svg width="22" height="16" viewBox="0 0 18 14"><rect width="18" height="14" rx="1" fill="#bbb"/><path d="M1 1l8 6 8-6" fill="none" stroke="#1c1c1c" stroke-width="1.5"/></svg>newsdesk@brawlpulse.co.nz</div>
</footer>

</body>
</html>
```